Banner dimension 1767 X 887 for Tolvenko website

Need one banner for our website www.tolvenko.com.au, The dimension of the banner should be 1767 x 887. Attached to this brief are two images that needs to be on that one banner, PLEASE DO NOT SEND SEPARATE BANNERS, both images on the same banner. Thanks

The banner should have the following message on it:

1.) " Take a further 40% off all stock" ( use code: TOLVENKO. Ends 31/12/2015)
2.) " Kick back or kick it up a notch this Autumn in the most versatile pique striped polo shirts and Pinafore belt strap denim dress"

Target Market(s)

kids aged 5-12yrs

Requirements
Must have
• very playful

```html
<!DOCTYPE html>
<html lang="en">
<head>
<meta charset="utf-8">
<title>Tolvenko Kids Wear – Sale Banners</title>
<link href="https://fonts.googleapis.com/css2?family=Oswald:wght@500;600;700&display=swap" rel="stylesheet">
<style>
  :root {
    --page: #ffffff;
    --cork: #c79a62;
    --cork-dark: #b3834c;
    --note-yellow: #f7ef7e;
    --paper-white: #f4f4f6;
    --ink-teal: #17586a;
    --sky-blue: #4ec3ea;
    --pin-red: #e0241f;
    --pin-green: #1ea64a;
    --gold-light: #f3c94a;
    --gold-dark: #b27a14;
    --splash-light: #c6eef6;
    --splash-mid: #8fd7ea;
  }
  * { box-sizing: border-box; margin: 0; padding: 0; }
  html, body { width: 1200px; height: 1000px; overflow: hidden; background: var(--page); }
  body { position: relative; font-family: "Oswald", sans-serif; }

  .banner { position: absolute; left: 202px; width: 844px; overflow: hidden; }
  .banner--cork { top: 54px; height: 422px; background: radial-gradient(circle at 30% 40%, var(--cork) 0%, var(--cork-dark) 100%); }
  .banner--splash {
    top: 523px; height: 440px;
    background:
      radial-gradient(ellipse at 20% 30%, rgba(255,170,60,.45) 0%, transparent 35%),
      radial-gradient(ellipse at 75% 35%, rgba(90,200,80,.35) 0%, transparent 30%),
      radial-gradient(ellipse at 40% 80%, rgba(70,80,200,.35) 0%, transparent 35%),
      radial-gradient(ellipse at 85% 85%, rgba(240,80,120,.25) 0%, transparent 30%),
      linear-gradient(135deg, var(--splash-light), var(--splash-mid));
  }

  .photo { position: absolute; z-index: 1; border-radius: 40px 40px 10px 10px; }
  .photo--boy { background: linear-gradient(180deg, #8a6a4c 0%, #2f6b4a 30%, #3a7556 45%, #9fb6c6 62%, #3a3a3a 100%); }
  .photo--girl { background: linear-gradient(180deg, #5a3a2a 0%, #f2f2f2 20%, #3d6a8a 35%, #56809e 70%, #e6b8a0 85%, #d9577a 100%); }

  .pin { position: absolute; z-index: 4; border-radius: 50%; }
  .pin--red { width: 22px; height: 22px; background: var(--pin-red); }
  .pin--green { width: 26px; height: 26px; background: var(--pin-green); }

  .sticky-note { position: absolute; z-index: 3; background: var(--note-yellow); box-shadow: 2px 4px 8px rgba(0,0,0,.25); text-align: center; color: var(--ink-teal); }
  .torn-paper { position: absolute; z-index: 3; background: var(--paper-white); box-shadow: 1px 3px 6px rgba(0,0,0,.2); color: var(--ink-teal); }

  .offer-line { font-weight: 700; text-transform: uppercase; line-height: 1; }
  .offer-percent { color: var(--sky-blue); font-weight: 700; line-height: 1; }
  .promo-code { font-size: 7.5px; color: var(--sky-blue); font-weight: 600; letter-spacing: .3px; }

  .tagline { font-weight: 600; text-transform: uppercase; line-height: 1.08; white-space: nowrap; }

  .brand { position: absolute; display: flex; align-items: center; gap: 4px; color: var(--ink-teal); font-weight: 600; }
  .brand__dot { width: 14px; height: 14px; border-radius: 50%; background: var(--ink-teal); }

  .headline {
    position: absolute; left: 0; width: 100%; top: 18px; text-align: center; z-index: 2;
    color: var(--ink-teal); font-weight: 700; text-transform: uppercase;
    font-size: 30px; line-height: 1; letter-spacing: .3px;
    text-shadow: 2px 0 #fff, -2px 0 #fff, 0 2px #fff, 0 -2px #fff, 2px 2px #fff, -2px -2px #fff, 2px -2px #fff, -2px 2px #fff;
  }
  .headline__percent {
    font-size: 66px; vertical-align: -8px;
    background: linear-gradient(180deg, var(--gold-light), var(--gold-dark));
    -webkit-background-clip: text; background-clip: text; color: transparent;
    text-shadow: none;
  }
</style>
</head>
<body>

  <section class="banner banner--cork">
    <div class="sticky-note" style="left:14px;top:14px;width:244px;height:242px;transform:rotate(-3deg);padding-top:52px;">
      <div class="offer-line" style="font-size:29px;">Take a further</div>
      <div class="offer-percent" style="font-size:64px;">40% <span style="color:var(--ink-teal);font-size:30px;">OFF</span></div>
      <div class="offer-line" style="font-size:29px;">All stock</div>
      <div class="promo-code" style="margin-top:22px;">( USE CODE: TOLVENKO. ENDS 31/12/2015)</div>
    </div>
    <div class="pin pin--red" style="left:126px;top:6px;"></div>

    <div class="torn-paper" style="left:22px;top:270px;width:402px;height:138px;transform:rotate(4deg);padding:16px 20px 0 50px;">
      <p class="tagline" style="font-size:20px;">Kick back or kick it up a notch<br>this summer in the most versatile<br>pique striped polo shirts and<br>pinafore belt strap denim dress"</p>
      <div class="brand" style="right:14px;bottom:6px;font-size:13px;"><span class="brand__dot"></span>Tolvenko</div>
    </div>
    <div class="pin pin--green" style="left:30px;top:316px;"></div>
    <div class="pin pin--green" style="left:376px;top:336px;"></div>

    <div class="photo photo--boy" role="img" aria-label="Boy in a green and black striped polo shirt and denim shorts, playfully posing" style="left:400px;top:6px;width:210px;height:416px;"></div>
    <div class="photo photo--girl" role="img" aria-label="Smiling girl in a white tee and denim pinafore dress with pink sneakers" style="left:656px;top:4px;width:150px;height:418px;"></div>
  </section>

  <section class="banner banner--splash" role="img" aria-label="Colourful abstract paint splash background">
    <h1 class="headline">" Take a further <span class="headline__percent">40%</span> off all stock"</h1>

    <div class="photo photo--boy" role="img" aria-label="Boy in a green and black striped polo shirt and denim shorts, playfully posing" style="left:0;top:82px;width:243px;height:358px;"></div>
    <div class="photo photo--girl" role="img" aria-label="Smiling girl in a white tee and denim pinafore dress with pink sneakers" style="left:648px;top:132px;width:164px;height:308px;"></div>

    <div class="sticky-note" style="left:282px;top:112px;width:310px;height:298px;transform:rotate(-2deg);padding:62px 10px 0 24px;text-align:left;">
      <p class="tagline" style="font-size:23.5px;font-weight:700;line-height:1.3;">Kick back or kick it up<br>a notch this summer in<br>the most versatile pique<br>striped polo shirts and<br>pinafore belt strap denim<br>dress"</p>
      <div class="brand" style="right:30px;bottom:50px;font-size:15px;"><span class="brand__dot"></span>Tolvenko</div>
      <div class="promo-code" style="position:absolute;left:0;right:0;bottom:14px;text-align:center;color:var(--ink-teal);">( USE CODE: TOLVENKO. ENDS 31/12/2015)</div>
    </div>
    <div class="pin pin--red" style="left:436px;top:98px;"></div>
  </section>

</body>
</html>
```